web site update

I want to get a better website for a small high end remodeling and construction company
I currently have a web site but you will find that it is not good.
www.quenbrickhall.com
We are a high end construction / remodeling company that has been in business since 2003. We primarily work in the mid peninsula of the bay area. Most of our clientele are very educated captains of industry. This group is still the target client.
I had my logo designed by Mint Easel a few years ago and I do like it, I like the orange and black or orange a blue. I don’t have a lot of content on hand as far as professional photographs.
Number of pages not sure and are open to: design pages vs full function website
I think what I am after is a web presence that will seal the deal as we are getting high referrals from past clients.
Construction
1 page

```html
<!DOCTYPE html>
<html lang="en">
<head>
<meta charset="utf-8">
<title>Quenbrick Hall Remodeling</title>
<link href="https://fonts.googleapis.com/css2?family=Open+Sans:wght@400;600;700;800&display=swap" rel="stylesheet">
<style>
:root{
  --orange:#f26a1b;
  --navy:#173a7d;
  --navy-dark:#102c63;
  --blue:#1f4f9e;
  --ink:#333a44;
  --muted:#7c828b;
  --light:#eeeff1;
  --line:#d9dbde;
  --white:#ffffff;
}
*{box-sizing:border-box;margin:0;padding:0}
html,body{width:687px;height:1200px;overflow:hidden}
body{font-family:"Open Sans",Arial,sans-serif;color:var(--ink);background:var(--white);position:relative}

/* header */
.site-header{position:absolute;left:0;top:0;width:687px;height:72px;background:var(--white)}
.brand{position:absolute;left:82px;top:8px;display:flex;align-items:center;gap:7px}
.brand-mark{width:32px;height:32px;background:var(--orange)}
.brand-name{font-weight:800;font-size:12px;line-height:13px;color:var(--navy);text-transform:uppercase;letter-spacing:.3px}
.phone{position:absolute;right:78px;top:10px;font-size:11px;font-weight:700;color:var(--navy);display:flex;align-items:center;gap:5px}
.phone-icon{width:14px;height:14px;border-radius:50%;background:var(--orange);display:flex;align-items:center;justify-content:center}
.main-nav{position:absolute;right:78px;top:44px;display:flex}
.main-nav a{font-size:8px;font-weight:700;color:var(--ink);text-decoration:none;padding:6px 9px;letter-spacing:.3px}
.main-nav a.active{color:var(--orange);border-bottom:2px solid var(--orange)}

/* hero */
.hero{position:absolute;left:0;top:72px;width:687px;height:244px;background:linear-gradient(100deg,#b9a48c 0%,#8c7560 35%,#6e6a5c 60%,#5d6a50 100%)}
.hero-copy{position:absolute;right:100px;top:160px;text-align:right;color:var(--white);font-size:15px;line-height:18px;font-weight:600;text-shadow:0 1px 3px rgba(0,0,0,.5)}
.hero-cta{position:absolute;right:100px;top:205px;height:26px;display:flex;align-items:center;background:var(--navy);color:var(--white);font-size:11px;font-weight:700;padding:0 14px 0 0}
.hero-cta .cta-icon{width:30px;height:26px;background:var(--orange);display:flex;align-items:center;justify-content:center;margin-right:10px}

/* services */
.services{position:absolute;left:0;top:316px;width:687px;height:200px;background:linear-gradient(#f7f7f8,#e4e5e7)}
.service-card{position:absolute;top:32px;width:176px;height:160px;background:var(--white);box-shadow:0 2px 6px rgba(0,0,0,.15);text-align:center;padding:16px 14px 0}
.service-card .icon{width:34px;height:34px;margin:0 auto 10px;display:block}
.service-card h3{font-size:10px;font-weight:800;color:var(--blue);line-height:12px;text-transform:uppercase}
.service-card h3 span{color:var(--orange)}
.service-card p{font-size:6px;color:var(--muted);line-height:9px;margin-top:6px}
.service-card .more{position:absolute;right:0;bottom:0;width:16px;height:16px;background:#9aa0a7;color:var(--white);font-size:12px;line-height:15px;font-weight:700}

/* welcome */
.welcome{position:absolute;left:95px;top:522px;width:497px;height:96px;text-align:center}
.welcome h2{font-size:12px;font-weight:800;color:var(--navy)}
.welcome h2 span{color:var(--orange)}
.rule{width:30px;height:2px;background:var(--orange);margin:5px auto 9px}
.welcome p{font-size:7px;line-height:11px;color:var(--muted);text-align:left}
.read-more{position:absolute;right:0;top:76px;font-size:7.5px;font-weight:700;color:var(--orange)}

/* gallery */
.gallery-title{position:absolute;left:0;top:625px;width:687px;height:20px}
.gallery-title .bar{position:absolute;left:0;top:9px;width:687px;height:2px;background:var(--navy)}
.gallery-title .tab{position:absolute;left:275px;top:0;width:138px;height:20px;background:var(--navy);color:var(--white);font-size:9px;font-weight:800;text-align:center;line-height:20px;letter-spacing:.4px}
.gallery{position:absolute;left:0;top:645px;width:687px;height:165px;background:var(--light)}
.gallery-item{position:absolute;top:48px;width:116px;height:105px}
.gallery-caption{position:absolute;left:0;bottom:10px;background:var(--navy);color:var(--white);font-size:6px;padding:3px 6px}
.gallery-arrow{position:absolute;top:88px;width:16px;height:16px;border-radius:50%;background:var(--white);border:1px solid var(--line);display:flex;align-items:center;justify-content:center}

/* testimonials */
.testimonials-title{position:absolute;left:0;top:826px;width:687px;text-align:center;font-size:12px;font-weight:800;color:var(--navy)}
.testimonials-title span{color:var(--orange)}
.testimonial{position:absolute;left:95px;top:860px;width:497px;height:72px;background:var(--white);border:1px solid var(--line);box-shadow:0 2px 4px rgba(0,0,0,.08)}
.testimonial .quote{position:absolute;left:8px;top:0;font-size:26px;color:#b9bdc2;font-weight:800}
.testimonial p{position:absolute;left:28px;top:12px;width:385px;font-size:6.5px;line-height:10px;color:var(--muted)}
.avatar{position:absolute;left:522px;top:858px;width:44px;height:44px;border-radius:50%;background:linear-gradient(#c8ccd2,#8c949e);border:2px solid var(--white);box-shadow:0 1px 4px rgba(0,0,0,.3)}
.testimonial-name{position:absolute;left:497px;top:942px;font-size:6.5px;color:var(--muted);font-style:italic}
.dots{position:absolute;left:95px;top:952px;display:flex;gap:4px}
.dots i{width:5px;height:5px;border-radius:50%;background:#c3c6ca}
.dots i:first-child{background:var(--navy)}

/* footer */
.site-footer{position:absolute;left:0;top:978px;width:687px;height:222px;background:var(--navy)}
.footer-col{position:absolute;top:18px;color:var(--white)}
.footer-col h4{font-size:9px;font-weight:800;letter-spacing:.3px;margin-bottom:12px}
.links li{list-style:none;font-size:7px;color:#d3dbec;margin-bottom:8px;display:flex;align-items:center;gap:5px}
.links li::before{content:"";width:3px;height:3px;background:var(--orange)}
.field{width:92px;height:14px;background:var(--white);font-size:6px;color:var(--muted);padding:3px 5px;margin-bottom:6px}
.field.area{height:30px}
.submit{width:36px;height:13px;background:var(--orange);color:var(--white);font-size:6px;font-weight:700;text-align:center;line-height:13px}
.contact-line{display:flex;gap:6px;font-size:6.5px;line-height:9px;color:#d3dbec;margin-bottom:9px}
.contact-line .ci{width:9px;height:9px;border-radius:50%;background:var(--orange);flex:none;margin-top:1px}
.social{position:absolute;left:512px;top:18px;display:flex;gap:5px}
.social i{width:15px;height:15px;border-radius:50%;background:#3d63b0}
.footer-brand{position:absolute;left:530px;top:100px;width:38px;height:38px;background:#2c519a}
.copyright{position:absolute;left:488px;top:158px;width:120px;font-size:6px;line-height:9px;color:#b9c5de;text-align:center}
.footer-bottom{position:absolute;left:0;bottom:0;width:687px;height:22px;background:var(--navy-dark)}
</style>
</head>
<body>

<header class="site-header">
  <div class="brand">
    <div class="brand-mark"></div>
    <div class="brand-name">Quenbrick Hall<br>Remodeling</div>
  </div>
  <div class="phone">
    <span class="phone-icon"><svg width="8" height="8" viewBox="0 0 24 24"><path fill="#fff" d="M6.6 10.8a15 15 0 0 0 6.6 6.6l2.2-2.2c.3-.3.7-.4 1-.2 1.1.4 2.3.6 3.6.6.6 0 1 .4 1 1V20c0 .6-.4 1-1 1A17 17 0 0 1 3 4c0-.6.4-1 1-1h3.5c.6 0 1 .4 1 1 0 1.3.2 2.5.6 3.6.1.3 0 .7-.2 1z"/></svg></span>
    415.555.0142
  </div>
  <nav class="main-nav">
    <a class="active">HOME</a><a>ABOUT US</a><a>SERVICES</a><a>GALLERY</a><a>CONTACT US</a>
  </nav>
</header>

<section class="hero" role="img" aria-label="Smiling family of three in front of a remodeled home">
  <div class="hero-copy">We Are The Leaders In<br>Remodeling And Construction Field</div>
  <div class="hero-cta">
    <span class="cta-icon"><svg width="12" height="12" viewBox="0 0 24 24"><path fill="#fff" d="M6.6 10.8a15 15 0 0 0 6.6 6.6l2.2-2.2c.3-.3.7-.4 1-.2 1.1.4 2.3.6 3.6.6.6 0 1 .4 1 1V20c0 .6-.4 1-1 1A17 17 0 0 1 3 4c0-.6.4-1 1-1h3.5c.6 0 1 .4 1 1 0 1.3.2 2.5.6 3.6.1.3 0 .7-.2 1z"/></svg></span>
    CALL US TODAY
  </div>
</section>

<section class="services">
  <div class="service-card" style="left:80px">
    <svg class="icon" viewBox="0 0 34 34"><rect width="34" height="34" rx="3" fill="#f26a1b"/><path d="M7 17 17 8l10 9" fill="none" stroke="#fff" stroke-width="2.5"/><rect x="11" y="16" width="12" height="11" fill="#fff"/><rect x="15" y="20" width="4" height="7" fill="#f26a1b"/></svg>
    <h3>Residential<br><span>Construction</span></h3>
    <p>Lorem ipsum dolor sit amet, consectetur adipiscing elit, sed diam nonummy nibh euismod.</p>
    <div class="more">+</div>
  </div>
  <div class="service-card" style="left:256px">
    <svg class="icon" viewBox="0 0 34 34"><rect width="34" height="34" rx="3" fill="#f26a1b"/><path d="M8 26 26 26 8 8z" fill="none" stroke="#fff" stroke-width="2.5"/><path d="M12 22h5l-5-5z" fill="#fff"/></svg>
    <h3>Property<br><span>Renovations</span></h3>
    <p>Lorem ipsum dolor sit amet, consectetur adipiscing elit, sed diam nonummy nibh euismod.</p>
    <div class="more">+</div>
  </div>
  <div class="service-card" style="left:432px">
    <svg class="icon" viewBox="0 0 34 34"><rect width="34" height="34" rx="3" fill="#f26a1b"/><rect x="9" y="8" width="14" height="6" fill="#fff" transform="rotate(35 16 11)"/><rect x="15" y="13" width="3" height="15" fill="#fff" transform="rotate(35 16 11)"/></svg>
    <h3>Complete<br><span>Refurbishments</span></h3>
    <p>Lorem ipsum dolor sit amet, consectetur adipiscing elit, sed diam nonummy nibh euismod.</p>
    <div class="more">+</div>
  </div>
</section>

<section class="welcome">
  <h2>WELCOME TO <span>QUENBRICK HALL</span> REMODELING</h2>
  <div class="rule"></div>
  <p>Lorem ipsum dolor sit amet, consectetuer adipiscing elit, sed diam nonummy nibh euismod tincidunt ut laoreet dolore magna aliquam erat volutpat. Ut wisi enim ad minim veniam, quis nostrud exerci tation ullamcorper suscipit lobortis nisl ut aliquip ex ea commodo consequat. Duis autem vel eum iriure dolor in hendrerit in vulputate velit esse molestie consequat, vel illum dolore eu feugiat nulla facilisis at vero eros et accumsan.</p>
  <div class="read-more">Read More »</div>
</section>

<div class="gallery-title"><div class="bar"></div><div class="tab">PROJECT GALLERY</div></div>
<section class="gallery">
  <div class="gallery-arrow" style="left:48px"><svg width="6" height="8" viewBox="0 0 6 8"><path d="M5 0 1 4l4 4" fill="none" stroke="#555" stroke-width="1.5"/></svg></div>
  <div class="gallery-item" role="img" aria-label="Remodeled kitchen with white cabinets" style="left:95px;background:linear-gradient(#d9d4cb,#8a7f70)"><div class="gallery-caption">Lorem ipsum dolor sit</div></div>
  <div class="gallery-item" role="img" aria-label="Open living room with large windows" style="left:222px;background:linear-gradient(#e6e2da,#a59a88)"></div>
  <div class="gallery-item" role="img" aria-label="Kitchen island with wood cabinetry" style="left:349px;background:linear-gradient(#cfc6b8,#6e5d4a)"></div>
  <div class="gallery-item" role="img" aria-label="Kitchen with dark wood cabinets and range" style="left:476px;background:linear-gradient(#b49a7e,#5c3f2c)"></div>
  <div class="gallery-arrow" style="left:623px"><svg width="6" height="8" viewBox="0 0 6 8"><path d="M1 0l4 4-4 4" fill="none" stroke="#555" stroke-width="1.5"/></svg></div>
</section>

<h2 class="testimonials-title"><span>CLIENT</span> TESTIMONIALS</h2>
<div class="testimonial">
  <div class="quote">“</div>
  <p>Lorem ipsum dolor sit amet, consectetuer adipiscing elit, sed diam nonummy nibh euismod tincidunt ut laoreet dolore magna aliquam erat volutpat. Ut wisi enim ad minim veniam, quis nostrud exerci tation ullamcorper suscipit lobortis nisl ut aliquip ex ea commodo consequat. Duis autem vel eum iriure dolor in hendrerit in vulputate velit esse molestie consequat.</p>
</div>
<div class="avatar" role="img" aria-label="Client portrait"></div>
<div class="testimonial-name">Mark D., Atherton, USA</div>
<div class="dots"><i></i><i></i><i></i></div>

<footer class="site-footer">
  <div class="footer-col" style="left:95px">
    <h4>QUICK LINKS</h4>
    <ul class="links"><li>Home</li><li>About Us</li><li>Services</li><li>Gallery</li><li>Contact Us</li></ul>
  </div>
  <div class="footer-col" style="left:190px">
    <h4>QUICK INQUIRY</h4>
    <div class="field">Name</div>
    <div class="field">Email</div>
    <div class="field area">Message</div>
    <div class="submit">SUBMIT</div>
  </div>
  <div class="footer-col" style="left:300px;width:120px">
    <h4>CONTACT DETAILS</h4>
    <div class="contact-line"><span class="ci"></span><span>Quenbrick Hall Remodeling<br>48 Laurel Avenue, Suite 12<br>San Mateo, CA 94401</span></div>
    <div class="contact-line"><span class="ci"></span><span>415.555.0142</span></div>
    <div class="contact-line"><span class="ci"></span><span>415.555.0143</span></div>
    <div class="contact-line"><span class="ci"></span><span>hello@quenbrickhall.com</span></div>
  </div>
  <div class="social"><i></i><i></i><i></i><i></i></div>
  <div class="footer-brand"></div>
  <div class="copyright">Copyright © 2016 Quenbrick Hall Remodeling<br>All Rights Reserved</div>
  <div class="footer-bottom"></div>
</footer>

</body>
</html>
```